Brennick Holdings Business Cards

These are professional business cards that are for my family office.
Put fake emails and phone numbers as of now until I finalize those components. This family office controls my families investments, assets, and future. The cards should be professional.
..
.
.
.
I just uploaded another variation of a logo I would like to see as a business card to I am inbeteen which logo to use

Target Market(s)

business

Industry/Entity Type

business

Contact Information for Business Card

Professional, wealth related, finance related.

Requirements
Must have
• Logo

```html
<!DOCTYPE html>
<html lang="en">
<head>
<meta charset="utf-8">
<title>Brennick Holdings Business Cards</title>
<link rel="stylesheet" href="https://fonts.googleapis.com/css2?family=Cinzel:wght@400;700&display=swap">
<style>
  :root {
    --backdrop: #3b3b3b;
    --card-dark: #2f2f2f;
    --card-light: #ffffff;
    --ink-light: #ffffff;
    --ink-navy: #1b2132;
    --ink-muted: #e6e6e6;
  }
  * { margin: 0; padding: 0; box-sizing: border-box; }
  html, body {
    width: 1200px; height: 803px; overflow: hidden;
    background: var(--backdrop);
  }
  .stage { position: relative; width: 1200px; height: 803px; }
  .card {
    position: absolute; width: 520px; height: 300px;
    border-radius: 22px; overflow: hidden;
    box-shadow: 0 18px 40px rgba(0,0,0,0.35);
  }
  .card--back { left: 80px; top: 100px; background: var(--card-dark); color: var(--ink-light); }
  .card--front { left: 610px; top: 405px; background: var(--card-light); color: var(--ink-navy); }

  .back-details { position: absolute; left: 36px; top: 70px; width: 260px; }
  .company {
    font-family: "Cinzel", serif; font-weight: 400; font-size: 22px;
    letter-spacing: 0.5px; margin-bottom: 14px;
  }
  .person-name {
    font-family: "Cinzel", serif; font-weight: 700; font-size: 19px; letter-spacing: 0.5px;
  }
  .person-role {
    font-family: Arial, Helvetica, sans-serif; font-size: 11px; color: var(--ink-muted);
    margin-bottom: 10px;
  }
  .address, .contact-list {
    font-family: Arial, Helvetica, sans-serif; font-size: 12px; line-height: 16px; color: var(--ink-muted);
  }
  .address { margin-bottom: 8px; }
  .contact-list { list-style: none; }
  .contact-list li { display: flex; align-items: center; gap: 8px; }
  .contact-list svg { width: 10px; height: 10px; flex: none; }

  .back-ring { position: absolute; right: 40px; top: 40px; width: 220px; height: 220px; }

  .front-mark { position: absolute; left: 50%; top: 34px; transform: translateX(-50%); width: 150px; height: 150px; }
  .front-name {
    position: absolute; left: 0; right: 0; top: 200px; text-align: center;
    font-family: "Cinzel", serif; font-weight: 400; font-size: 32px; letter-spacing: 1px;
  }
</style>
</head>
<body>
<main class="stage">
  <section class="card card--back">
    <div class="back-details">
      <p class="company">Brennick Holdings</p>
      <p class="person-name">Adrian Coles</p>
      <p class="person-role">President</p>
      <p class="address">4120 Harrow Crescent<br>Millbrook, Canada 21860</p>
      <ul class="contact-list">
        <li><svg viewBox="0 0 10 10"><path d="M2 1l2 0 1 2-1 1c.6 1.2 1.5 2 2.5 2.5l1-1 2 1v2c-4 .5-8-3.5-7.5-7.5z" fill="currentColor"/></svg>555-214-8830</li>
        <li><svg viewBox="0 0 10 10"><rect x="1" y="1" width="8" height="8" fill="none" stroke="currentColor" stroke-width="1.2"/></svg>555-319-4472</li>
        <li><svg viewBox="0 0 10 10"><rect x="1" y="2" width="8" height="6" fill="none" stroke="currentColor" stroke-width="1.2"/><path d="M1 2l4 3 4-3" fill="none" stroke="currentColor" stroke-width="1.2"/></svg>info@brennickholdings.com</li>
        <li><svg viewBox="0 0 10 10"><circle cx="5" cy="5" r="4" fill="currentColor"/></svg>www.brennickholdings.com</li>
      </ul>
    </div>
    <svg class="back-ring" viewBox="0 0 220 220" aria-hidden="true">
      <circle cx="110" cy="110" r="104" fill="none" stroke="var(--ink-light)" stroke-width="5"/>
    </svg>
  </section>

  <section class="card card--front">
    <svg class="front-mark" viewBox="0 0 150 150" aria-hidden="true">
      <circle cx="75" cy="75" r="70" fill="none" stroke="var(--ink-navy)" stroke-width="3"/>
    </svg>
    <p class="front-name">Brennick Holdings</p>
  </section>
</main>
</body>
</html>
```